Online Art Gallery & Art Management Firm looking for a business card

I'm launching an online art gallery (paintings, photography, drawings, furniture, books, ...) where people can buy all types of art. It's a platform where young and unknown artists can showcase their oeuvre.

Additionally, the venture will act as my advising company for artists. I help them out with their business side of life and become their representative.

The company name: The Velvet Parlour
Logo is attached

I'm looking for something very classy and upmarket.
Updates

Reason: Logo wasn't finished yet...

The design should include the following information: - Name: Pieter Vandomme - Title: Founder - Mobile: +32 (0) 486 514 362 - E-mail: pieter@velvet-parlour.example - Website www.velvet-parlour.example I prefer the have the logo (without website) on the one side and the information on the other. Best regards Pieter

Target Market(s)

Art buyers / art dealers / artists / middle class / upmarket /

Industry/Entity Type

Artists

Colors

Designer to choose colors to be used in the design.

Requirements
Must have
• Must communicate credibility, trust and integrity
Nice to have
• Something classy, chique
Should not have
• Nothing to artistic or creative

```html
<!DOCTYPE html>
<html lang="en">
<head>
<meta charset="utf-8">
<title>The Velvet Parlour – Business Card</title>
<link rel="stylesheet" href="https://fonts.googleapis.com/css2?family=Ubuntu:wght@300;400&display=swap">
<style>
  :root {
    --backdrop: #2e2b2a;
    --card-light: #fbfbfa;
    --card-dark: #050505;
    --ink-dark: #1c1c1c;
    --ink-light: #f2f2f2;
    --frame-line: #8a8a8a;
  }
  * { box-sizing: border-box; margin: 0; padding: 0; }
  html, body {
    width: 1200px;
    height: 1200px;
    overflow: hidden;
    background: var(--backdrop);
    font-family: "Ubuntu", sans-serif;
  }
  .canvas {
    position: relative;
    width: 1200px;
    height: 1200px;
  }
  .card {
    position: absolute;
    left: 270px;
    width: 660px;
    height: 370px;
    box-shadow: 0 12px 30px rgba(0,0,0,0.35);
  }
  .card--front {
    top: 170px;
    background: var(--card-light);
    display: flex;
    align-items: center;
    justify-content: center;
  }
  .brand-name {
    font-weight: 300;
    font-size: 26px;
    letter-spacing: 6px;
    color: var(--ink-dark);
    text-transform: uppercase;
  }
  .card--back {
    top: 640px;
    background: var(--card-dark);
    color: var(--ink-light);
  }
  .brand-box {
    position: absolute;
    top: 30px;
    right: 30px;
    width: 170px;
    height: 150px;
    border: 1px solid var(--frame-line);
    display: flex;
    align-items: flex-end;
    justify-content: center;
    padding-bottom: 18px;
  }
  .brand-box .brand-name {
    font-size: 11px;
    letter-spacing: 1.6px;
    color: var(--ink-light);
  }
  .contact {
    position: absolute;
    left: 56px;
    top: 150px;
  }
  .contact__first {
    font-weight: 300;
    font-size: 44px;
    line-height: 1;
  }
  .contact__last {
    font-weight: 300;
    font-size: 30px;
    line-height: 1.3;
  }
  .contact__title {
    font-size: 20px;
    margin-left: 6px;
  }
  .contact__details {
    margin-top: 14px;
    display: grid;
    grid-template-columns: 58px auto;
    column-gap: 16px;
    row-gap: 2px;
    font-weight: 300;
    font-size: 15px;
    line-height: 1.3;
  }
</style>
</head>
<body>
  <main class="canvas">
    <section class="card card--front" aria-label="Card front">
      <span class="brand-name">The Velvet Parlour</span>
    </section>

    <section class="card card--back" aria-label="Card back">
      <div class="brand-box">
        <span class="brand-name">The Velvet Parlour</span>
      </div>
      <div class="contact">
        <p class="contact__first">Pieter</p>
        <p class="contact__last">Vandomme<span class="contact__title">Founder</span></p>
        <div class="contact__details">
          <span>Mobile</span><span>+32 (0) 486 514 362</span>
          <span>Email</span><span>pieter@velvet-parlour.example</span>
          <span></span><span>www.velvet-parlour.example</span>
        </div>
      </div>
    </section>
  </main>
</body>
</html>
```